5 x 7 card advertising ash spreading

I need a new design for a double sided 5 x 7 horizontal post card to give to funeral homes so they can give them out to people who are interested in an ash spreading boat charter at sea for their loved one who has died. I want a simple, professional, classy, thoughtful design that I can include a summary of what we offer, what's included, our logo and and contact info. Even though we will include the "what" we offer, this piece needs to speak to the readers "why". I've included an AI excerpt about why people desire this as opposed to being buried.
What we offer: Attended service, Unattended service, Memorial service, Anniversary service. What's included: Certificate of Ash Spreading, Onboard refreshments, Personalized music. Our contact information: Tidewell Charters, www.tidewellcharters.example, 452 Marlowe St., Clearwater, FL 33755, (727) 555-0148

Target Market(s)

People visiting a funeral home planning their own or a relatives final wishes for ash spreading at sea

Industry/Entity Type

Private boat charters

Requirements
Must have
• Professional look, speaks to they "why", as well as includes the "what" we do.

```html
<!DOCTYPE html>
<html lang="en">
<head>
<meta charset="utf-8">
<title>Tidewell Charters – A Loving Farewell at Sea</title>
<link rel="stylesheet" href="https://fonts.googleapis.com/css2?family=DM+Serif+Display&family=Playfair+Display:ital@1&family=Jost:wght@400;500;600;700&display=swap">
<style>
  :root {
    --navy: #1c2c5b;
    --navy-deep: #1a2a57;
    --gold: #d7bc93;
    --frame-gold: #c9b08a;
    --mist: #e3eaf2;
    --paper: #ffffff;
    --backdrop: #e5e6e7;
  }
  * { margin: 0; padding: 0; box-sizing: border-box; }
  html, body { width: 1200px; height: 829px; overflow: hidden; background: var(--backdrop); }
  body { position: relative; font-family: "Jost", sans-serif; color: var(--navy); }

  .card { position: absolute; top: 34px; width: 543px; height: 761px; overflow: hidden; }
  .card-front { left: 49px; }
  .card-back { left: 610px; background: var(--paper); }
  .frame { position: absolute; inset: 17px; border: 1px solid var(--frame-gold); pointer-events: none; z-index: 5; }

  /* Front */
  .sea-photo {
    position: absolute; inset: 0;
    background: linear-gradient(180deg, #b9c7da 0%, #c8c3d2 18%, #d9b9c2 30%, #9aa2c0 44%, #6d7cab 58%, #42548b 74%, #2b3a6b 100%);
  }
  .brand { position: absolute; display: flex; align-items: center; gap: 6px; font-family: "Jost", sans-serif; font-weight: 600; color: var(--navy); z-index: 6; }
  .brand-dot { width: 14px; height: 14px; border-radius: 50%; background: var(--navy); flex: none; }
  .card-front .brand { left: 34px; top: 78px; font-size: 15px; }
  .headline { position: absolute; left: 0; width: 100%; text-align: center; line-height: 1; }
  .headline-serif { font-family: "DM Serif Display", serif; color: var(--navy); font-size: 92px; letter-spacing: -1px; }
  .line-loving { top: 148px; left: 10px; }
  .line-farewell { top: 219px; left: 6px; }
  .line-sea { top: 300px; font-family: "Playfair Display", serif; font-style: italic; color: #fff; font-size: 84px; left: 0; }
  .tagline { position: absolute; left: 0; width: 100%; top: 656px; text-align: center; color: #fff; font-size: 24px; line-height: 31px; font-weight: 400; letter-spacing: 0.3px; }

  /* Back */
  .back-shapes { position: absolute; inset: 0; }
  .card-back .brand { left: 36px; top: 96px; font-size: 12px; width: 90px; line-height: 1.1; }
  .why-title { position: absolute; top: 48px; left: 150px; width: 290px; text-align: center; font-weight: 700; font-size: 23px; line-height: 28px; letter-spacing: 0.2px; }
  .why-copy { position: absolute; top: 120px; left: 70px; width: 405px; text-align: center; font-size: 11.6px; line-height: 15px; }
  .why-copy p + p { margin-top: 15px; }

  .offer-title { position: absolute; top: 374px; left: 0; width: 100%; text-align: center; color: var(--gold); font-weight: 700; font-size: 22px; letter-spacing: 1.5px; }
  .offer-intro { position: absolute; top: 407px; left: 60px; width: 423px; text-align: center; color: #fff; font-size: 12px; line-height: 15px; }
  .offer-list { position: absolute; list-style: none; color: #fff; font-size: 8.8px; line-height: 9.6px; }
  .offer-list li { position: relative; padding-left: 13px; margin-bottom: 10px; }
  .offer-list li::before { content: "↓"; position: absolute; left: 0; top: -1px; font-size: 9px; }
  .offer-list strong { display: block; font-weight: 700; }
  .services { left: 79px; top: 456px; width: 175px; }
  .included { left: 296px; top: 485px; width: 170px; }
  .included-label { position: absolute; left: 310px; top: 456px; color: #fff; font-weight: 700; font-size: 8.8px; }
  .col-divider { position: absolute; left: 272px; top: 468px; width: 1px; height: 143px; background: var(--gold); }
  .contact-rule { position: absolute; left: 85px; top: 638px; width: 383px; height: 1px; background: var(--gold); }
  .contact { position: absolute; left: 0; width: 100%; top: 650px; text-align: center; color: #fff; }
  .contact-title { color: var(--gold); font-weight: 700; font-size: 22px; letter-spacing: 1.5px; line-height: 28px; }
  .contact-address { font-size: 11.5px; line-height: 15px; margin-top: 1px; }
  .contact-phone { font-weight: 700; font-size: 15px; letter-spacing: 1px; line-height: 19px; }
  .contact-email { font-size: 11px; letter-spacing: 0.8px; line-height: 14px; }
</style>
</head>
<body>
  <section class="card card-front">
    <div class="sea-photo" role="img" aria-label="Photograph of calm ocean water at dusk under a pastel pink and blue sky, with a single white flower floating on the surface"></div>
    <div class="brand"><span class="brand-dot"></span>Tidewell Charters</div>
    <h1>
      <span class="headline headline-serif line-loving">A Loving</span>
      <span class="headline headline-serif line-farewell">Farewell</span>
      <span class="headline line-sea">at Sea</span>
    </h1>
    <p class="tagline">Honoring Loved Ones With<br>Grace and Serenity at Sea</p>
    <div class="frame"></div>
  </section>

  <section class="card card-back">
    <svg class="back-shapes" width="543" height="761" viewBox="0 0 543 761" aria-hidden="true">
      <ellipse cx="272" cy="250" rx="285" ry="68" fill="var(--mist)"/>
      <path d="M0 318 Q272 372 543 318 L543 761 L0 761 Z" fill="var(--navy-deep)"/>
      <path d="M0 312 Q272 366 543 312 L543 322 Q272 380 0 324 Z" fill="var(--gold)"/>
      <path d="M258 346 L272 305 L284 346 Z" fill="var(--navy-deep)"/>
      <rect x="236" y="346" width="70" height="3" fill="var(--navy-deep)"/>
    </svg>
    <div class="brand"><span class="brand-dot"></span>Tidewell Charters</div>
    <h2 class="why-title">WHY CHOOSE ASH SPREADING AT SEA?</h2>
    <div class="why-copy">
      <p>At Tidewell Charters, we understand that saying goodbye to a loved one is a deeply personal and emotional journey. Spreading ashes at sea is a timeless tradition that offers serenity, closure, and connection with nature. The open waters symbolize freedom, peace, and eternity—creating a meaningful and beautiful farewell.</p>
      <p>Our compassionate team is here to provide you with a respectful, stress-free experience, ensuring every detail reflects your wishes. Whether you want an intimate attended service or a simple unattended ceremony, we handle everything with care and dignity, giving you peace of mind during this important moment.</p>
    </div>

    <h2 class="offer-title">WHAT WE OFFER</h2>
    <p class="offer-intro">At Tidewell Charters, we provide dignified ash-spreading services, including attended or unattended ceremonies, memorials, and anniversary services.</p>
    <ul class="offer-list services">
      <li><strong>Attended Service</strong>A private ceremony at sea where family and friends can participate.</li>
      <li><strong>Unattended Service</strong>For those who cannot attend, we ensure the ashes are spread with care and provide you with a certificate.</li>
      <li><strong>Memorial Service</strong>Celebrate your loved one with music, readings, and refreshments in a peaceful setting.</li>
      <li><strong>Anniversary Service</strong>Mark the anniversary of their passing with a special tribute at sea.</li>
    </ul>
    <div class="col-divider"></div>
    <p class="included-label">What's Included:</p>
    <ul class="offer-list included">
      <li><strong>Certificate of Ash Spreading</strong>A meaningful keepsake to commemorate the ceremony.</li>
      <li><strong>Onboard Refreshments</strong>Comfort for your guests during the journey.</li>
      <li><strong>Personalized Music</strong>Create the perfect atmosphere with songs that hold special meaning.</li>
    </ul>
    <div class="contact-rule"></div>
    <address class="contact" style="font-style:normal">
      <div class="contact-title">CONTACT US:</div>
      <div class="contact-address">452 Marlowe St., Clearwater, FL 33755</div>
      <div class="contact-phone">(727) 555-0148</div>
      <div class="contact-email">info@tidewellcharters.example</div>
    </address>
    <div class="frame"></div>
  </section>
</body>
</html>
```